Become an EMT and Serve your community!

We are looking to design a postcard that will be mailed to surrounding communities that notifies them of our upcoming EMT class with an emphasis of serving their community. We are looking for a design that grabs peoples attention and motivates them to sign up and serve their community. Our primary colors are red and blue. We would like to incorporate the Institute logo as well as one or two photos. We do have more photos available upon request. Our Institute website is www.halvorsenacademy.net for more material. It is important that the postcard meets mailing guidelines.

Target Market(s)

Local community members

Industry/Entity Type

Education

Font styles to use
Sans Serif

Colors
f04a50
3176b5
0255a3
eaf1f7

Requirements
Must have
• Dates
Prices
Contact info
Look interesting
Convey the message of “Serving your Community”
Nice to have
• Clear information
Concise
Incorporate an action shot
Should not have
• Generic EMS logos

```html
<!DOCTYPE html>
<html lang="en">
<head>
<meta charset="utf-8">
<title>Summer EMT Class 2020 Postcard</title>
<link href="https://fonts.googleapis.com/css2?family=Pacifico&family=Josefin+Sans:wght@300;400;600;700&family=Arimo:wght@400;700&display=swap" rel="stylesheet">
<style>
  :root{
    --red:#f04a50;
    --blue:#0255a3;
    --blue-mid:#3176b5;
    --ice:#eaf1f7;
    --white:#ffffff;
    --ink:#2a2a2a;
    --page:#ececec;
    --font-script:'Pacifico', cursive;
    --font-head:'Josefin Sans', sans-serif;
    --font-body:'Arimo', sans-serif;
  }
  *{box-sizing:border-box;margin:0;padding:0}
  html,body{width:1200px;height:903px;overflow:hidden;background:var(--page)}
  .sheet{position:relative;width:1200px;height:903px}
  .card{position:absolute;left:220px;width:760px;height:414px;background:var(--white);overflow:hidden;box-shadow:0 2px 8px rgba(0,0,0,.15)}
  .card--front{top:20px}
  .card--back{top:469px}

  /* front */
  .front-photo{position:absolute;left:300px;top:0;width:460px;height:414px;
    background:linear-gradient(100deg,#d9d9d9 0%,#eeeeee 35%,#c9a98a 55%,#d44a4e 80%,#e9e9e9 100%)}
  .title-block{position:absolute;left:0;top:0;width:380px;height:173px;background:var(--red);border-bottom-right-radius:70px;color:var(--white);text-align:center}
  .title-script{font-family:var(--font-script);font-size:60px;line-height:1;position:absolute;left:32px;top:8px;width:330px;text-align:center}
  .title-class{font-family:var(--font-head);font-weight:700;font-size:27px;letter-spacing:7px;position:absolute;left:60px;top:95px;width:310px}
  .title-year{font-family:var(--font-head);font-weight:300;font-size:34px;letter-spacing:13px;position:absolute;left:60px;top:126px;width:310px}
  .serve-block{position:absolute;left:0;top:195px;width:380px;height:219px;background:var(--blue);border-top-right-radius:60px;color:var(--white)}
  .serve-word{font-family:var(--font-head);font-size:29px;letter-spacing:17px;position:absolute;left:40px;top:20px;width:300px;text-align:center}
  .serve-sub{font-family:var(--font-head);font-size:24px;letter-spacing:2px;position:absolute;left:34px;top:54px;width:320px;text-align:center}
  .serve-body{font-family:var(--font-body);font-size:13.4px;line-height:16.6px;position:absolute;left:26px;top:85px;width:350px}
  .learn-more{position:absolute;left:122px;top:178px;width:104px;height:22px;border:1.5px solid var(--white);font-family:var(--font-head);font-size:12px;letter-spacing:2px;text-align:center;line-height:21px}
  .brand-mark{position:absolute;left:395px;top:14px;display:flex;align-items:center;gap:6px;font-family:var(--font-head);font-weight:700;font-size:13px;color:var(--blue)}
  .brand-mark .dot{width:12px;height:12px;border-radius:50%;background:var(--red)}

  /* back */
  .action-photo{position:absolute;left:0;top:0;width:255px;height:414px;background:linear-gradient(160deg,#bdbdbd 0%,#6e6e6e 45%,#9a9a9a 70%,#3c3c3c 100%)}
  .tab{position:absolute;left:261px;height:37px;background:var(--red);border-bottom-right-radius:28px;color:var(--white);font-family:var(--font-head);font-size:20px;letter-spacing:1.5px;padding:11px 0 0 17px;width:171px}
  .tab-box{position:absolute;left:261px;background:var(--blue);border-top-right-radius:28px;color:var(--white);font-family:var(--font-head);font-size:12px;line-height:13px;letter-spacing:.5px;padding:6px 0 0 12px;width:171px}
  .tab--when{top:17px}
  .box--when{top:58px;height:62px}
  .tab--tuition{top:217px}
  .box--tuition{top:258px;height:63px}
  .back-title{position:absolute;left:446px;top:24px;width:165px;text-align:center}
  .back-title .title-script{position:static;width:auto;font-size:34px;color:var(--red)}
  .back-title .class{font-family:var(--font-head);font-weight:700;font-size:16px;letter-spacing:4px;color:var(--blue);margin-top:2px}
  .back-title .year{font-family:var(--font-head);font-weight:300;font-size:18px;letter-spacing:7px;color:var(--ink)}
  .stamp{position:absolute;left:655px;top:21px;width:76px;height:100px;border:1.5px solid #bdbdbd}
  .schedule{position:absolute;left:272px;top:131px;width:480px;font-family:var(--font-head);font-size:11.6px;line-height:13px;color:var(--ink)}
  .schedule p+p{margin-top:13px}
  .mission{position:absolute;left:463px;top:228px;width:290px;color:var(--blue)}
  .mission h3{font-family:var(--font-head);font-weight:400;font-size:18px;letter-spacing:1.5px}
  .mission p{font-family:var(--font-body);font-size:10.6px;line-height:13.5px;margin-top:2px;color:var(--blue-mid)}
  .cut-line{position:absolute;left:272px;top:341px;width:460px;border-top:1.5px dashed var(--red)}
  .contact{position:absolute;top:353px;font-family:var(--font-head);font-size:11.6px;line-height:15px;color:var(--ink)}
  .contact--address{left:300px}
  .contact--lines{left:475px}
  .contact-row{display:flex;align-items:center;gap:8px}
  .icon{width:12px;height:12px;flex:none}
  .home-icon{position:absolute;left:277px;top:369px;width:14px;height:14px}
</style>
</head>
<body>
<main class="sheet">

  <section class="card card--front">
    <div class="front-photo" role="img" aria-label="Smiling EMT in a red polo shirt with a stethoscope, in front of an open ambulance"></div>
    <div class="brand-mark"><span class="dot"></span>Halvorsen Academy</div>
    <div class="title-block">
      <div class="title-script">Summer</div>
      <div class="title-class">EMT CLASS</div>
      <div class="title-year">2020</div>
    </div>
    <div class="serve-block">
      <div class="serve-word">SERVING</div>
      <div class="serve-sub">YOUR COMMUNITY</div>
      <p class="serve-body">and become an Emergency Medical Technician. As a student you will have access to cutting edge training equipment, experienced instructors, and be able to train on a 911 Ambulance through Halvorsen EMS.</p>
      <div class="learn-more">Learn more</div>
    </div>
  </section>

  <section class="card card--back">
    <div class="action-photo" role="img" aria-label="Black and white photo of students practising CPR on a training manikin"></div>

    <div class="tab tab--when">When</div>
    <div class="tab-box box--when">Monday, Tuesday,<br>Wednesday<br>from May 26th<br>through August 17th.</div>

    <div class="back-title">
      <div class="title-script">Summer</div>
      <div class="class">EMT CLASS</div>
      <div class="year">2020</div>
    </div>
    <div class="stamp"></div>

    <div class="schedule">
      <p>Wednesdays: Students will need to sign up for either a<br>4:00p-7:00p lab section, or a 7:00p-10:0p lab section.</p>
      <p>There will be one required Sat/Sun weekend held for all students.<br>This will take place on June 13th &amp; 14th.<br>Weekend classes will run from 8:00am - 8:00pm.</p>
    </div>

    <div class="tab tab--tuition">Tuition</div>
    <div class="tab-box box--tuition">$1000 EMT<br>(without CPR).<br>$250 deposit is due<br>at time of registration.</div>

    <div class="mission">
      <h3>Serving your Community</h3>
      <p>and become an Emergency Medical Technician.<br>As a student you will have access<br>to cutting edge training equipment,<br>experienced instructors, and be able to train<br>on a 911 Ambulance through Halvorsen EMS.</p>
    </div>

    <div class="cut-line"></div>

    <svg class="home-icon" viewBox="0 0 14 14" fill="none" stroke="#2a2a2a" stroke-width="1.3"><path d="M1.5 7 7 2l5.5 5M3 6v6h8V6M6 12V9h2v3"/></svg>
    <div class="contact contact--address">Halvorsen Academy of EMS<br>18 Linden Street<br>Bristow, NH 03999</div>
    <div class="contact contact--lines">
      <div class="contact-row"><svg class="icon" viewBox="0 0 12 12" fill="none" stroke="#2a2a2a" stroke-width="1.2"><path d="M1 4c0-2 10-2 10 0v1H8V4H4v1H1zM3 6h6l1 5H2z"/></svg>T: 603-555-0142&nbsp;&nbsp;F: 603-555-0187</div>
      <div class="contact-row"><svg class="icon" viewBox="0 0 12 12" fill="none" stroke="#2a2a2a" stroke-width="1.1"><circle cx="6" cy="6" r="5"/><ellipse cx="6" cy="6" rx="2.2" ry="5"/><path d="M1 6h10"/></svg>Director@halvorsenacademy.net</div>
      <div class="contact-row"><svg class="icon" viewBox="0 0 12 12" fill="none" stroke="#2a2a2a" stroke-width="1.1"><rect x="1" y="2.5" width="10" height="7"/><path d="m1 2.5 5 4 5-4"/></svg>www.halvorsenacademy.net</div>
    </div>
  </section>

</main>
</body>
</html>
```